Riverpeak Analytics needs new design business card

We are video surveillance and analytics software development company.
I am looking for a professional business card.
Our website is www.riverpeakanalytics.example.au
Please have a loo and get the feel for who we are and what we do.
I do not know what else to give you apart from good luck and I hope your design gets selected.
Thank you very much for participating
Business
Contact Information for Business Card
Address
27/15 Marlowe Street Fernbrook NSW 2199
Telephone 1300 582 417
Mobile 0450 731 258
email: marcus@riverpeakanalytics.example.au
name
Marcus Helvard
Position
Managing Director
Font styles to use
Other font styles liked:
- Arial
Look and feel

```html
<!DOCTYPE html>
<html lang="en">
<head>
<meta charset="utf-8">
<title>Riverpeak Analytics – Business Card</title>
<link rel="stylesheet" href="https://fonts.googleapis.com/css2?family=Open+Sans:wght@400;600;700&display=swap">
<style>
  :root {
    --backdrop: #2b2b2d;
    --card: #ffffff;
    --navy: #1f4a86;
    --band-blue: #1b5ea6;
    --band-grey: #a9abae;
    --accent: #f5a623;
    --ink-light: #ffffff;
  }
  * { margin: 0; padding: 0; box-sizing: border-box; }
  html, body { width: 1200px; height: 659px; overflow: hidden; }
  body {
    background: var(--backdrop);
    font-family: "Open Sans", Arial, sans-serif;
    position: relative;
  }
  .card {
    position: absolute;
    width: 520px;
    height: 300px;
    background: var(--card);
    overflow: hidden;
    box-shadow: 0 10px 30px rgba(0,0,0,.45);
  }
  .card--back { left: 50px; top: 180px; }
  .card--front { left: 630px; top: 180px; }

  .wordmark {
    position: absolute;
    display: flex;
    align-items: center;
    gap: 12px;
    color: var(--navy);
    font-weight: 700;
    font-size: 30px;
    letter-spacing: .5px;
    white-space: nowrap;
  }
  .wordmark__square { width: 26px; height: 26px; background: var(--navy); }

  .back-band {
    position: absolute; left: 0; top: 78px;
    width: 100%; height: 144px;
    background: var(--band-grey);
  }
  .card--back .wordmark { left: 50%; top: 150px; transform: translate(-50%, -50%); }

  .card--front .wordmark { left: 70px; top: 52px; }
  .front-shapes { position: absolute; inset: 0; }

  .person {
    position: absolute; right: 16px; top: 131px; text-align: right;
  }
  .person__name { color: var(--ink-light); font-weight: 700; font-size: 18px; line-height: 22px; }
  .person__role { color: var(--accent); font-size: 12px; line-height: 16px; margin-top: 2px; }

  .contacts {
    position: absolute; left: 22px; top: 192px;
    list-style: none; color: var(--ink-light);
    font-size: 12.5px; line-height: 15.5px;
  }
  .contacts li { display: flex; align-items: center; gap: 8px; }
  .contacts svg { width: 11px; height: 11px; flex: none; }

  .address {
    position: absolute; right: 22px; bottom: 12px;
    color: var(--navy); font-weight: 700; font-size: 13px;
  }
</style>
</head>
<body>
  <section class="card card--back" aria-label="Card back">
    <div class="back-band"></div>
    <div class="wordmark"><span class="wordmark__square"></span>Riverpeak Analytics</div>
  </section>

  <section class="card card--front" aria-label="Card front">
    <svg class="front-shapes" viewBox="0 0 520 300" aria-hidden="true">
      <polygon points="0,195 235,195 262,150 520,150 520,262 0,262" fill="var(--band-blue)"/>
      <polygon points="272,128 520,128 520,150 262,150" fill="var(--band-grey)"/>
      <rect x="240" y="166" width="120" height="20" fill="var(--band-grey)"/>
    </svg>

    <div class="wordmark"><span class="wordmark__square"></span>Riverpeak Analytics</div>

    <div class="person">
      <p class="person__name">Marcus Helvard</p>
      <p class="person__role">Managing Director</p>
    </div>

    <ul class="contacts">
      <li>
        <svg viewBox="0 0 12 12"><path d="M2 1h3l1 3-1.5 1a6 6 0 0 0 2.5 2.5L8 6l3 1v3a1 1 0 0 1-1 1A9 9 0 0 1 1 2a1 1 0 0 1 1-1z" fill="var(--accent)"/></svg>
        1300 582 417
      </li>
      <li>
        <svg viewBox="0 0 12 12"><rect x="3" y="0.5" width="6" height="11" rx="1" fill="none" stroke="var(--accent)" stroke-width="1.3"/></svg>
        0450 731 258
      </li>
      <li>
        <svg viewBox="0 0 12 12"><circle cx="6" cy="6" r="5" fill="none" stroke="var(--accent)" stroke-width="1.2"/><path d="M1 6h10M6 1c-2.5 3-2.5 7 0 10M6 1c2.5 3 2.5 7 0 10" fill="none" stroke="var(--accent)" stroke-width="1"/></svg>
        www.riverpeakanalytics.example.au
      </li>
      <li>
        <svg viewBox="0 0 12 12"><rect x="0.7" y="2" width="10.6" height="8" fill="none" stroke="var(--accent)" stroke-width="1.2"/><path d="M1 2.5l5 4 5-4" fill="none" stroke="var(--accent)" stroke-width="1.2"/></svg>
        marcus@riverpeakanalytics.example.au
      </li>
    </ul>

    <p class="address">27/15 Marlowe Street Fernbrook NSW 2199</p>
  </section>
</body>
</html>
```